Personal Card: Make it roar!

Hello to all designers,
Hope you're having a nice day/evening! Let's cut to the chase. I would like a modern, beautiful and professional personal business card; with a vector-art of a lion. I'd like the lion to be Blood Red. On a black background. I'm a Filipino, and would love to have my country's flag incorporated into the design. Id like the stars of my flag to be used in your designs if possible. The texts I want on the card are only my name, number, and email address. Colour of my name should be White, and my details Silver. The size and font should be simple and professional, you're in charge of that! The placements of the lion and my details will be yours to decide.

At the back of the card, I would like just the words "Thank You" (Silver) on a Black Background. Right on the center.

To summarise, my requirements are:
- Blood Red: Front Face of Lion, Vector-Art
- Black: Background
- Yellow: Three Stars used in the design
- White: Benedict Sr Talavera
- Silver: Number & Email (Where appropriate)
- Back of the card (Center). Silver: "Thank You"
- Please DON'T use the colour blue.

It's all about the Lion. Images you'll find attached are some images of Lions' faces which I particularly want to be captured and put onto the card. Convert it into a vector-art. A vector-art Lion. PLEASE use the images attached for inspiration only! Do not use it on your designs. Thank you very much for your time.

Good luck!

Ben
Updates

Hello Desginers, Please use Blood Red for the colour red in your designs:HEX: 8A0707RGB: 138,7,7Thank you,Ben Added Saturday, March 12, 2016

Target Market(s)

Potential Connections

Industry/Entity Type

It Professional

Contact Information for Business Card

Name: Benedict Sr Talavera
Email: bentalavera@mailhaven.co.uk
Number: 07382614927

Requirements
Must have
• Modern, Professional & Simple
• (Blood Red HEX: 8A0707, RGB: 138,7,7) Lion (Vector-style art)
• (Black) Background
• (White) My Name
• (Silver) My Details
• Back of card: "Thank You" in Silver. Font size should be small/medium.
• Only colours that should be used are Red, Black, Yellow and White/Silver
Nice to have
• - Use of 3 Yellow stars on the design
Should not have
• - Please avoid using any other colours apart from those specified.

```html
<!DOCTYPE html>
<html lang="en">
<head>
<meta charset="utf-8">
<title>Benedict Sr Talavera – Business Card</title>
<link rel="stylesheet" href="https://fonts.googleapis.com/css2?family=Cinzel:wght@400;700&family=Cormorant+Garamond:wght@500&display=swap">
<style>
  :root {
    --page-bg: #d9d6d1;
    --card-black: #141414;
    --blood-red: #8a0707;
    --blood-red-deep: #4a0303;
    --name-white: #ffffff;
    --detail-silver: #b9b9b9;
    --detail-silver-dim: #8f8f8f;
    --card-shadow: rgba(0, 0, 0, 0.28);
  }

  * { box-sizing: border-box; margin: 0; padding: 0; }

  html, body {
    width: 1200px;
    height: 800px;
    overflow: hidden;
  }

  body {
    background: var(--page-bg);
    display: flex;
    align-items: center;
    justify-content: center;
    gap: 40px;
  }

  .card {
    width: 540px;
    height: 309px;
    background: var(--card-black);
    box-shadow: 0 14px 34px var(--card-shadow);
    position: relative;
  }

  /* Back face */
  .card--back {
    display: flex;
    align-items: center;
    justify-content: center;
  }

  .thank-you {
    font-family: "Cinzel", serif;
    font-weight: 400;
    font-size: 25px;
    letter-spacing: 0.16em;
    color: var(--detail-silver);
    text-transform: uppercase;
  }

  /* Front face */
  .card--front {
    display: flex;
    flex-direction: column;
    align-items: center;
  }

  .lion-art {
    margin-top: 22px;
    width: 190px;
    height: 170px;
    border-radius: 48% 48% 44% 44%;
    background: radial-gradient(ellipse at 50% 52%, var(--card-black) 0%, var(--blood-red-deep) 38%, var(--blood-red) 62%, rgba(138, 7, 7, 0.55) 100%);
  }

  .contact {
    margin-top: 10px;
    text-align: center;
    display: flex;
    flex-direction: column;
    align-items: center;
    gap: 3px;
  }

  .contact__name {
    font-family: "Cinzel", serif;
    font-weight: 700;
    font-size: 17px;
    letter-spacing: 0.2em;
    color: var(--name-white);
    text-transform: uppercase;
  }

  .contact__phone,
  .contact__email {
    font-family: "Cormorant Garamond", serif;
    font-weight: 500;
    font-size: 13px;
    letter-spacing: 0.12em;
    text-transform: uppercase;
  }

  .contact__phone { color: var(--detail-silver); }
  .contact__email { color: var(--detail-silver-dim); }
</style>
</head>
<body>
  <section class="card card--back">
    <p class="thank-you">Thank You</p>
  </section>

  <section class="card card--front">
    <div class="lion-art" role="img" aria-label="Blood red vector illustration of a lion's face with an ornate mane"></div>
    <div class="contact">
      <h1 class="contact__name">Benedict Sr Talavera</h1>
      <p class="contact__phone">07382614927</p>
      <p class="contact__email">bentalavera@mailhaven.co.uk</p>
    </div>
  </section>
</body>
</html>
```